Online travel site needs edgy website design

tripvane is the first Global Business Travel Website that provides the most comprehensive destination information tailored to suit the business traveller.

It is a ‘one click solution’ that offers direct access to all aspects of business travel, including general information on the city, accommodation and transportation options, economic and financial statistics, key business and services contacts, as well as leisure activities, entertainment suggestions, and listings for any personal needs.

Much more than a travel website, tripvane.com eliminates the need to buy multiple travel books or visit scores of websites. Most importantly, it is the only website that will cover such an extensive range of destinations around the world, while also featuring cities where information is really scarce. The user-friendly and consistent format for all destinations will allow the business traveller to easily navigate through more than 100 information pages on any destination.

tripvane will be simple to navigate, intuitive, unique in design, dynamic, and content rich providing a supreme user experience during navigation of the website.

The website will initially be English and is set to expand to more languages in the future.

A beta site with back-end database has been built - and now we need an edgy state of the art graphic design to reskin it.

LOOK & FEEL

Scope
The design of the site should reflect tripvane’s corporate and user centric philosophy with the following elements:

a. tripvane corporate image and branding
b. the promotion of each city destination
c. tripvane being the starting point of travel, while also a partner during travel
d. the subtle but powerful presence of advertising and sponsorship

All the above must derive from the design outline and elements that are going to be used.

Design Guidelines

Innovative and elegant design, minimalism, simplicity that permits the offering of the required information to be delivered in line with the values of Trust, Care, Discovery & Connection.

In addition:

1. The usability, navigation and the informative character of the corporate web site should not be compromised by the design.
2. The over-segmented pages and over-crowded content per page should be avoided.
3. The design should not only guide the user in an inviting way to the information required but also to intrigue them for further navigation.
4. Advertising space should be anticipated in line with the design character and DMQ standard ad sizes.
5. The use of photos / videos should also encouraged.

Key Elements

a. Branding/Logos
Throughout the website branding should be present as a “guarantee seal” for the content accuracy. Corporate logo should be placed on every page while branding should also characterise any content element and/or tool. Appendix contains the current brand guidelines. Should additional sub-logos be required for specific sections, these should be proposed.

b. Fonts
Provided your experience on the website design you are requested to propose alternative font types and sizes always taken into consideration the inviting and user friendly character that the new website should aspire to. The font type that will be proposed must be user friendly in English typography, but also could support other languages in the future.

Given the fact that the majority of the text in the website contains information and listing, the fonts and text layout should not strain and fatigue the reader.

c. SEO
The design should be friendly towards the search engines.

d. Colours
Colour is considered as an integral part of the brand identity. Tripvane.com corporate colours are orange and grey as per the Attached document reference guide.

Different tonalities of the brand colours, or colours in general, should be proposed and applied, guided always by the above described scope of Look & Feel.

e. Section Headings
As presented above, the site’s section headings (refer Overview of the Site.) The principle is to label the content following users’ needs and mindset. However, the label space should be flexible for changes. The labels should facilitate the user to understand the content they host. This is important and should be applied especially to informative content.

Another function that Headings should perform is that of promoting the website’s content, especially when this kind of content will make the user spend more time in the website. This category of Headings should be approached in a more creative and attractive way as to intrigue users to check the content hosted.

f. Icons
Icons are considered necessary in order to provide the user extra help to guide them to reach the information they need quick n’ easy. Icons not only contribute actively to the creation of an attractive look & feel but, most importantly, facilitate navigation and speed up the users’ familiarisation with the website too.

Therefore their design should be eye-catching, comprehensive and dynamic, in accordance to the new site’s colour coding and following the latest trends as these were defined by the look & feel of smart phones.

PIXELHIVE BRIEF REQUIREMENTS
Based on the above, please provide at least two (2) approaches for the following pages – this includes colour palette in line with logo, layout, fonts.

Initial submissions can just address Deliverable 1 & 2 to fine tune design before proceeding further.

Please refer sample screenshots separately attached from raw beta site for content – available for Deliverables 2 -6.

(REFER example sites we like for their creativity: http://www.brindle-studio.example.co.uk/#Background, http://www.rotaclarafestas.example.com.br/, http://pembrookweb.example.co.uk/ )

Deliverable 1: Landing /Home page
- Access log in –
o Free Account or via Workloop/Chatterbox etc
o Membership Access – Login
- How to use the site
- Allowance for video or animation
- Destination Selection
- Blog & Social media links

Deliverable 2: Destination Landing Page / Template
This is essentially a city guide template to be used for all cities throughout the site.

This page clearly depicts the four information sections
1. General
2. Business
3. Leisure
4. Personal

Also this page should include:
- Business News Feed
- Advertising & Sponsorship Spaces (according to DMQ Standards)
- Destination Time, Weather, FX rates (LIVE feeds)
- Tips

Deliverable 3: Follow the above format but show an Internal Content Page – text only with subheadings

Deliverable 4: Follow the above format but show an Internal Content Page – text and photos

Deliverable 5: Follow the above format but show an Internal Content Page – Listing Sections such as Restaurants (this must also include filter categories)

Deliverable 6: Follow the above format but show an Internal Content Page – Top 10 Experiences – this incorporates address and contact details, photo and sub-text

Deliverable 7: The Membership Landing Page which should include:
1. Intro
2. Advertising & Sponsorship Space
3. The four sections
4. Tips Section
Updates

Hi all - just to reiterate that we are open to different approaches in the design.  We only included the existing screen shots of the beta site to provide you with an idea of the content.  We definitely don't want to see anything similar.....we want it to be edgy yet simple and easy to navigate....we want to create an outstanding user experience!  Cheers Tripvane Team

Reason: Dear Designers - We are extending the period as have not had many submissions at all and want to provide more time. If you have already submitted, we will be in touch shortly with feedback. Thanks for your understanding Tripvane Team

Reason: We would like to give everyone more time so we can find the best and most preferred design.

Target Market(s)

TARGET MARKET
tripvane is a consumer focused website, offering a wide-range of easy-to-use and interactive platforms, for informative and commercial purposes, while also providing attractive and innovative advertising real-estate for potential business partners.

The target audience can be segmented as follows:

Primary Target: Professionals travelling on Business

They require up-to-date reliable information prior and during their travel, as well as facilitation to take action. They need an online Personal Assistant.

The personal characteristics of the primary target group are: busy life, tailored solutions, reliable sources, trusting, caring, and spoiled.
 
The website will have a membership option (for a small annual fee) which will provide customized information for their demographic and preferences. Sub target groups will include:
1. Business Men 40 years
3. Business Women 40 years
5. Business People with reduced mobility

Demographic & Travelling Profile of Business Travellers

• 92% of them use the internet as a source of info
• 54% are males, 38 years old
• 80% holds a college/university degree
• 68% is travelling mainly for leisure and annually 6 times per year
• 52% reserve their ticket through the internet
• 66% is travel internationally

Secondary Targets:

Executive PA’s
Executive personal assistants who need to plan their manager’s travel and provide support information for their trip.

Professionals travelling for Leisure and Partners
They have most probably used the website for their business travel, but consider it also useful for their leisure travel. The generic website, will include enough information to cover most of the leisure needs, as well as the requirements of their partners.

Direct Business-to-Business [B2B] Targets
The direct [B2B] targeted audience includes corporations that would like to use a white label solution for their staff, by using all available destinations or a selected number depending on their global network.

Business-to-Business [B2B] Targets
The [B2B] targeted audience is an indirect audience, for which tripvane promotes its services, and a key revenue stream. The B2B audience consists mainly of a diverse range of professional organisations targeting the business traveller (airlines, hotels, travel agencies, tourism authorities, entertainment companies, services, etc.) tripvane will be targeting these organisations to advertise on the site.
 
Desired Response from Target Groups

The desired response from the consumer targets is:
a) Recurrent use of website
b) Share content/experience with friends and social networking sites
c) Interact on the website’s Blog
d) Register for newsletters and offers
e) Subscribe to Membership
f) Be exposed to commercial advertisements on the website
g) Provide feedback (in the future) for services
h) Use (in the future) online services to purchase products and services
Competition

Industry/Entity Type

Travel

Requirements
Must have
• A clean crisp and professional appearance giving a sense of Trust and Reliability.
Should not have
• It should not look like every other run of the mill travel sites - Roomly.com, Wanderpost etc

```html
<!DOCTYPE html>
<html lang="en">
<head>
<meta charset="utf-8">
<title>tripvane — City Guide: Dubai</title>
<link rel="stylesheet" href="https://fonts.googleapis.com/css2?family=Lato:wght@300;400;700&display=swap">
<style>
:root{
  --orange:#f07a12;
  --orange-dark:#d9640a;
  --ink:#3a3a3a;
  --text:#333;
  --muted:#666;
  --grey-dark:#3d3d3d;
  --hero-top:#555;
  --hero-bottom:#3a3a3a;
  --page:#ffffff;
  --rule:#ececec;
  --teal:#27b0c4;
  --purple:#7a4ed6;
  --red:#e01f45;
  --green:#3ec836;
}
*{box-sizing:border-box;margin:0;padding:0}
html,body{width:1200px;height:1134px;overflow:hidden;background:var(--page);font-family:'Lato',sans-serif;color:var(--text)}
.site-header{height:85px;position:relative}
.brand{position:absolute;left:200px;top:24px;display:flex;align-items:center;gap:8px;text-decoration:none}
.brand-mark{width:36px;height:36px;background:var(--grey-dark);border-radius:4px}
.brand-name{font-size:36px;font-weight:700;color:var(--orange);letter-spacing:-1px;line-height:1}
.top-nav{position:absolute;right:200px;top:27px;display:flex;align-items:center}
.top-nav .nav-link{font-size:13px;color:var(--muted);margin-right:21px;text-decoration:none}
.btn{display:inline-block;height:29px;line-height:29px;font-size:13px;font-weight:700;color:#fff;text-align:center;text-decoration:none}
.btn-login{width:87px;background:var(--grey-dark);margin-right:9px}
.btn-signup{width:86px;background:var(--orange)}

.hero{position:absolute;left:0;top:85px;width:1200px;height:381px;background:linear-gradient(180deg,var(--hero-top) 0%,#4a4a4a 55%,var(--hero-bottom) 100%)}
.hero-title{position:absolute;left:236px;top:100px;font-size:52px;font-weight:300;color:#fff;letter-spacing:-3px}
.search{position:absolute;left:240px;top:154px;width:526px;height:41px;background:#fff;display:flex;align-items:center}
.search svg.lens{margin-left:13px}
.search input{border:0;outline:0;font:300 16px 'Lato',sans-serif;color:#888;margin-left:12px;width:400px;background:transparent}
.search-go{position:absolute;right:4px;top:4px;width:48px;height:33px;background:var(--orange);display:flex;align-items:center;justify-content:center}
.btn-video{position:absolute;left:771px;top:154px;width:180px;height:41px;background:var(--orange);display:flex;align-items:center;color:#fff;font-size:18px;font-weight:400;letter-spacing:-.5px;text-decoration:none}
.btn-video svg{margin:0 8px 0 16px}
.city-bar{position:absolute;left:374px;top:228px;width:450px;height:47px;background:rgba(0,0,0,.75);border:1px solid #222;display:flex;align-items:center;justify-content:center;gap:20px;color:#fff;font-weight:300;font-size:26px;letter-spacing:-1px}
.city-bar .stat{display:flex;align-items:center;gap:6px}
.city-bar small{font-size:12px;letter-spacing:0;font-weight:400;margin-top:8px}

.guide{position:absolute;left:200px;top:420px;width:800px;height:638px;background:#fff;box-shadow:0 0 3px rgba(0,0,0,.12)}
.sections{position:absolute;left:8px;top:7px;display:flex;gap:8px}
.section-tile{width:190px;height:80px;color:#fff;display:flex;flex-direction:column;align-items:center;justify-content:flex-end;padding-bottom:14px;font-size:20px;text-decoration:none}
.section-tile svg{margin-bottom:8px}
.tile-general{background:var(--teal)}
.tile-business{background:var(--purple)}
.tile-leisure{background:var(--red)}
.tile-personal{background:var(--green)}

h2{font-size:20px;font-weight:700;color:var(--ink)}
.overview{position:absolute;left:10px;top:102px;width:520px}
.overview p{font-size:11px;line-height:12.8px;margin-top:7px;color:#333}
.read-more{display:block;margin-top:7px;font-size:11px;font-weight:700;color:var(--orange);text-decoration:none}
.city-photos{position:absolute;left:538px;top:95px;width:255px;height:144px;display:flex}
.city-photos div{flex:1}
.photo-a{background:linear-gradient(135deg,#2a2a2a,#cfcfcf 60%,#444)}
.photo-b{background:linear-gradient(160deg,#1e8fd0,#5cc3e8 50%,#1a6aa8)}
.photo-c{background:linear-gradient(180deg,#1a2140,#2b3560 60%,#6a5a3a)}
.rule{position:absolute;left:10px;width:780px;height:1px;background:linear-gradient(90deg,transparent,var(--rule) 15%,var(--rule) 85%,transparent)}

.feed{position:absolute;top:272px;width:380px}
.feed-news{left:10px}
.feed-tips{left:406px}
.feed ul{list-style:none;margin-top:12px}
.feed li{display:flex;align-items:flex-start;height:45px}
.feed li p{font-size:11px;line-height:13.5px;margin-left:12px;margin-top:1px;color:#444}
.date-badge{position:relative;width:32px;height:29px;background:var(--orange);color:#fff;text-align:center;flex:none;margin-left:2px}
.date-badge b{display:block;font-size:14px;font-weight:400;line-height:15px;padding-top:2px}
.date-badge span{display:block;font-size:8px;line-height:9px}
.date-badge::after,.tip-icon::after{content:"";position:absolute;right:-5px;top:10px;border:5px solid transparent;border-right:0;border-left-color:inherit}
.date-badge{border-color:var(--orange)}
.tip-icon{position:relative;width:32px;height:29px;flex:none;display:flex;align-items:center;justify-content:center}
.tip-info{background:var(--teal);border-color:var(--teal)}
.tip-warn{background:var(--red);border-color:var(--red)}

.ad-banner{position:absolute;left:110px;top:463px;width:582px;height:72px;background:linear-gradient(90deg,#b9a98a 0%,#d7c8a6 35%,#3f9dc9 70%,#2a7fb5 100%)}
.partners{position:absolute;left:36px;top:565px;width:730px;height:60px;display:flex;align-items:center;justify-content:space-between}
.partner{background:#9a9a9a;opacity:.75}
.p-sq{width:44px;height:54px;border-radius:2px}
.p-wide{width:96px;height:18px;border-radius:9px}
.p-circ{width:36px;height:36px;border-radius:50%}

.site-footer{position:absolute;left:0;top:1074px;width:1200px;height:60px;border-top:1px solid #e3e3e3}
.copyright{position:absolute;left:200px;top:22px;font-size:11px;color:#666}
.social{position:absolute;left:470px;top:23px;display:flex;gap:10px;font-size:9px;color:#999}
.footer-nav{position:absolute;right:200px;top:22px;font-size:11px;color:#666}
.footer-nav a{color:#666;text-decoration:none}
.footer-nav i{font-style:normal;margin:0 7px;color:#999}
</style>
</head>
<body>
<header class="site-header">
  <a class="brand" href="#"><span class="brand-mark"></span><span class="brand-name">tripvane</span></a>
  <nav class="top-nav">
    <a class="nav-link" href="#">Blog</a>
    <a class="btn btn-login" href="#">LOGIN</a>
    <a class="btn btn-signup" href="#">SIGN UP</a>
  </nav>
</header>

<section class="hero" role="img" aria-label="Black and white photo of a city skyline at dusk">
  <h1 class="hero-title">On business to?</h1>
  <form class="search">
    <svg class="lens" width="22" height="22" viewBox="0 0 22 22"><circle cx="9" cy="9" r="6.5" fill="none" stroke="#888" stroke-width="3"/><line x1="14" y1="14" x2="20" y2="20" stroke="#888" stroke-width="3.5" stroke-linecap="round"/></svg>
    <input type="text" placeholder="Enter your destination" value="Enter your destination">
    <span class="search-go"><svg width="22" height="20" viewBox="0 0 22 20"><path d="M2 10h18M12 2l3 8-3 8M4 6l2 4-2 4" fill="none" stroke="#fff" stroke-width="2.6" stroke-linejoin="round"/></svg></span>
  </form>
  <a class="btn-video" href="#"><svg width="22" height="22" viewBox="0 0 22 22"><circle cx="11" cy="11" r="11" fill="#3d3d3d"/><path d="M9 7l6 4-6 4z" fill="#fff"/></svg>Watch our video</a>
  <div class="city-bar">
    <span class="stat"><svg width="18" height="18" viewBox="0 0 18 18"><circle cx="9" cy="9" r="7" fill="none" stroke="#fff" stroke-width="2.5"/><circle cx="9" cy="9" r="2.5" fill="#fff"/></svg>Dubai</span>
    <span class="stat"><svg width="26" height="18" viewBox="0 0 26 18"><circle cx="9" cy="6" r="4" fill="#fff"/><path d="M5 16a5 5 0 0 1 3-8 6 6 0 0 1 11 1 4 4 0 0 1 1 7z" fill="#fff"/></svg>36°C</span>
    <span class="stat"><svg width="18" height="18" viewBox="0 0 18 18"><circle cx="9" cy="9" r="7" fill="none" stroke="#fff" stroke-width="2.5"/><path d="M9 5v4h3" fill="none" stroke="#fff" stroke-width="2"/></svg>2:33<small>PM</small></span>
    <span class="stat"><svg width="18" height="18" viewBox="0 0 18 18"><circle cx="9" cy="9" r="8" fill="#fff"/><text x="9" y="13" text-anchor="middle" font-family="Lato,sans-serif" font-weight="700" font-size="11" fill="#000">$</text></svg>3.67<small>AED</small></span>
  </div>
</section>

<main class="guide">
  <nav class="sections">
    <a class="section-tile tile-general" href="#"><svg width="26" height="24" viewBox="0 0 26 24"><path d="M3 21L21 3M13 4l6 1 1 6M6 13l-3 1 3 3M8 18l1 3 3-3" fill="none" stroke="#fff" stroke-width="3" stroke-linecap="round"/></svg>General</a>
    <a class="section-tile tile-business" href="#"><svg width="28" height="24" viewBox="0 0 28 24"><rect x="1" y="6" width="26" height="17" rx="2" fill="#fff"/><rect x="9" y="1" width="10" height="6" rx="1.5" fill="none" stroke="#fff" stroke-width="2.5"/></svg>Business</a>
    <a class="section-tile tile-leisure" href="#"><svg width="28" height="26" viewBox="0 0 28 26"><path d="M5 9h18l-9 14z" fill="none" stroke="#fff" stroke-width="2.5" stroke-linejoin="round"/><path d="M5 9l4-4h10l4 4" fill="none" stroke="#fff" stroke-width="2.5"/><circle cx="4" cy="3" r="1.5" fill="#fff"/><circle cx="24" cy="3" r="1.5" fill="#fff"/></svg>Leisure</a>
    <a class="section-tile tile-personal" href="#"><svg width="34" height="24" viewBox="0 0 34 24"><circle cx="11" cy="6" r="5" fill="#fff"/><path d="M1 23a10 9 0 0 1 20 0z" fill="#fff"/><circle cx="23" cy="6" r="5" fill="#fff"/><path d="M23 14a10 9 0 0 1 10 9h-9" fill="#fff"/></svg>Personal</a>
  </nav>

  <article class="overview">
    <h2>City Overview</h2>
    <p>Aenean neque ipsum, feugiat sit amet luctus eu, varius et lorem. Cras non libero non magna dapibus molestie. Quisque dapibus imperdiet sapien eu imperdiet. Duis lacinia porta metus, id fringilla neque tempor quis. Curabitur ullamcorper metus vitae porttitor luctus. Nam vitae felis non metus euismod ullamcorper at in diam. Sed ac nulla sed ante luctus egestas sit amet in libero. Vivamus cursus, diam ornare posuere hendrerit, dolor augue facilisis enim, non suscipit tellus sem a nisl. Pellentesque ut adipiscing dui. In consectetur augue ipsum. Sed convallis neque magna, nec tempor arcu faucibus dapibus. Pellentesque commodo erat in eros sollicitudin, in euismod eros tempor. Nulla facilisi.</p>
    <a class="read-more" href="#">READ MORE</a>
  </article>
  <div class="city-photos">
    <div class="photo-a" role="img" aria-label="Close-up of a carved lattice window screen"></div>
    <div class="photo-b" role="img" aria-label="Aerial view of a sail-shaped hotel on the coast"></div>
    <div class="photo-c" role="img" aria-label="Tall tower lit up over the city at night"></div>
  </div>

  <div class="rule" style="top:256px"></div>

  <section class="feed feed-news">
    <h2>Business News Feed</h2>
    <ul>
      <li><span class="date-badge"><b>28</b><span>SEP</span></span><p>Lorem ipsum dolor sit amet, consectetuer adipiscing elit, sed diam nonummy nibh euismod tincidunt ut.</p></li>
      <li><span class="date-badge"><b>28</b><span>SEP</span></span><p>Lorem ipsum dolor sit amet, consectetuer adipiscing elit, sed diam nonummy nibh euismod tincidunt ut.</p></li>
      <li><span class="date-badge"><b>28</b><span>SEP</span></span><p>Lorem ipsum dolor sit amet, consectetuer adipiscing elit, sed diam nonummy nibh euismod tincidunt ut.</p></li>
    </ul>
  </section>
  <section class="feed feed-tips">
    <h2>Tips</h2>
    <ul>
      <li><span class="tip-icon tip-info"><svg width="14" height="12" viewBox="0 0 14 12"><ellipse cx="7" cy="5" rx="6" ry="4.5" fill="#fff"/><path d="M3 8l-1 4 4-3z" fill="#fff"/></svg></span><p>Lorem ipsum dolor sit amet, consectetuer adipiscing elit, sed diam nonummy nibh euismod tincidunt ut.</p></li>
      <li><span class="tip-icon tip-warn"><svg width="16" height="14" viewBox="0 0 16 14"><path d="M8 1l7 12H1z" fill="#fff"/><rect x="7.2" y="5" width="1.6" height="4.5" fill="#e01f45"/><rect x="7.2" y="10.5" width="1.6" height="1.5" fill="#e01f45"/></svg></span><p>Lorem ipsum dolor sit amet, consectetuer adipiscing elit, sed diam nonummy nibh euismod tincidunt ut.</p></li>
      <li><span class="tip-icon tip-info"><svg width="14" height="12" viewBox="0 0 14 12"><ellipse cx="7" cy="5" rx="6" ry="4.5" fill="#fff"/><path d="M3 8l-1 4 4-3z" fill="#fff"/></svg></span><p>Lorem ipsum dolor sit amet, consectetuer adipiscing elit, sed diam nonummy nibh euismod tincidunt ut.</p></li>
    </ul>
  </section>

  <div class="rule" style="top:452px"></div>

  <a class="ad-banner" href="#" role="img" aria-label="Sponsored banner: beach scene with colourful umbrellas promoting a city arts and nightlife trip in June"></a>

  <div class="rule" style="top:550px"></div>

  <div class="partners" aria-label="Sponsors and partners">
    <span class="partner p-sq"></span>
    <span class="partner p-wide"></span>
    <span class="partner p-circ"></span>
    <span class="partner p-wide" style="width:76px"></span>
    <span class="partner p-wide" style="width:80px"></span>
    <span class="partner p-wide" style="width:76px"></span>
    <span class="partner p-circ" style="width:40px;height:40px"></span>
    <span class="partner p-wide" style="width:76px"></span>
  </div>
</main>

<footer class="site-footer">
  <p class="copyright">© 2013 Tripvane.com &nbsp; All rights reserved.</p>
  <div class="social"><span>Chatterbox</span><span>Chirper</span><span>Workloop</span><span>Circles</span><span>RSS</span></div>
  <nav class="footer-nav"><a href="#">Blog</a><i>|</i><a href="#">Privacy Policy</a><i>|</i><a href="#">Terms &amp; Conditions</a><i>|</i><a href="#">Jobs</a><i>|</i><a href="#">Contact Us</a></nav>
</footer>
</body>
</html>
```